New Business Card Design Project

I would like my card design to look exactly like the logo, design, layout, and print of the current attached file. The only change I would like made would be for the print to say THE KMW GROUP instead of THE HALLORAN GROUP. Basically, just replace his group name with my group name. I would also like the backgroud to be the same texture and color as the attached file. I love the dark blue lettering and house logo on the card.

I am completely open to the rest of the card design. I just want something clean and simple. Only basic contact info required on the card. Maybe just name: Kyle M Warrick and cell # 555.914.2087 and email kyle@orchidhomesagent.com

```html
<!DOCTYPE html>
<html lang="en">
<head>
<meta charset="utf-8">
<title>The KMW Group – Business Card</title>
<link href="https://fonts.googleapis.com/css2?family=Lato:wght@400;700;900&display=swap" rel="stylesheet">
<style>
  :root {
    --navy: #171729;
    --paper: #f2f2f3;
    --page: #ffffff;
    --ink-light: #f2f2f3;
  }
  * { margin: 0; padding: 0; box-sizing: border-box; }
  html, body {
    width: 1200px; height: 1200px; overflow: hidden;
    background: var(--page);
    font-family: "Lato", sans-serif;
  }
  .canvas { position: relative; width: 1200px; height: 1200px; }
  .card {
    position: absolute; top: 271px; width: 382px; height: 630px;
    border-radius: 22px;
  }
  .card--front { left: 203px; background: var(--navy); color: var(--ink-light); }
  .card--back { left: 599px; background: var(--paper); color: var(--navy); }

  .brand { position: absolute; display: flex; align-items: center; }
  .brand__square { background: currentColor; }
  .brand__name {
    font-weight: 400; line-height: 1.2; text-transform: uppercase;
  }
  .card--front .brand { left: 56px; top: 251px; gap: 30px; }
  .card--front .brand__square { width: 96px; height: 96px; }
  .card--front .brand__name { font-size: 27px; letter-spacing: 5px; line-height: 31px; }
  .card--back .brand { left: 86px; top: 125px; gap: 24px; }
  .card--back .brand__square { width: 74px; height: 74px; }
  .card--back .brand__name { font-size: 21px; letter-spacing: 4px; line-height: 24px; }

  .website {
    position: absolute; left: 0; right: 0; top: 581px;
    text-align: center; font-size: 11px; letter-spacing: 3px;
  }

  .person { position: absolute; left: 0; right: 0; top: 297px; text-align: center; }
  .person__name { font-size: 25px; font-weight: 900; letter-spacing: 0.5px; }
  .person__title { font-size: 15px; font-weight: 700; margin-top: 1px; }

  .contact {
    position: absolute; left: 0; right: 0; top: 427px;
    list-style: none; text-align: center; font-size: 20px; line-height: 33px;
  }
  .contact__item { display: flex; justify-content: center; align-items: center; gap: 10px; }
  .contact__icon { width: 18px; height: 18px; fill: none; stroke: var(--navy); stroke-width: 1.6; }
  .contact__icon--solid { fill: var(--navy); stroke: none; }
</style>
</head>
<body>
<main class="canvas">
  <section class="card card--front">
    <div class="brand">
      <span class="brand__square"></span>
      <span class="brand__name">The<br>KMW<br>Group</span>
    </div>
    <p class="website">www.orchidhomesagent.com</p>
  </section>

  <section class="card card--back">
    <div class="brand">
      <span class="brand__square"></span>
      <span class="brand__name">The<br>KMW<br>Group</span>
    </div>
    <div class="person">
      <h1 class="person__name">KYLE M WARRICK</h1>
      <p class="person__title">MANAGER</p>
    </div>
    <ul class="contact">
      <li class="contact__item">
        <svg class="contact__icon contact__icon--solid" viewBox="0 0 20 20" aria-hidden="true">
          <path d="M2 7c0-2 3-4 8-4s8 2 8 4v2h-4V7.5c-1-.6-2.5-1-4-1s-3 .4-4 1V9H2z"/>
          <path d="M5 10l2-3h6l2 3v6H5z"/>
        </svg>
        <span>555.914.2087</span>
      </li>
      <li class="contact__item">
        <svg class="contact__icon" viewBox="0 0 20 20" aria-hidden="true">
          <rect x="2" y="5" width="16" height="11"/>
          <path d="M2 5l8 6 8-6"/>
        </svg>
        <span>kyle@orchidhomesagent.com</span>
      </li>
    </ul>
  </section>
</main>
</body>
</html>
```